Brantley Advisory Group provides support for renewable energy projects to utilities and suppliers

I need a professional looking business card that is both simple and elegant and unique. My clients are mostly large organizations not individuals. I am a consultant with my own company that is small but would like to give clients the impression I am larger. Smart grid, fiber optics, software, field hardware, distribution automation, substation automation, operations, energy storage/batteries, microgrids, customer service, strategy/roadmaps, conservation, Automated Metering Infrastruture (AMI or smart meters) are all areas of focus.

Target Market(s)

Utilities, suppliers, governmental agencies involved in energy. All types of energy especially natural gas and electrical. Especially renewable energy or green projects.

Contact Information for Business Card

Name - Mark Brantley Cell Phone - 425.318.2746 Email - mbrantley@brantleyag-example.com
Company - Brantley Advisory Group (logo) Title - Principal

Font styles to use
Serif
Sans Serif

Colors

Designer to choose colors to be used in the design.

Requirements
Must have
• Simple and professional and powerful.
• Unique/creative design.
Nice to have
• Utilize color scheme to accent logo colors. Maybe some geometric pattern on edge of card with color.
Should not have
• Busy, complicated, traditional

```html
<!DOCTYPE html>
<html lang="en">
<head>
<meta charset="utf-8">
<title>Brantley Advisory Group – Business Card</title>
<link href="https://fonts.googleapis.com/css2?family=Lato:wght@400;700&family=Noto+Serif:wght@700&display=swap" rel="stylesheet">
<style>
  :root {
    --backdrop: #232323;
    --card-light: #ebebea;
    --card-light-edge: #f1f1ef;
    --brand-blue: #1a1a8e;
    --brand-blue-soft: #21219a;
    --brand-green: #5b8a3c;
    --text-grey: #4a4a4a;
    --white: #ffffff;
  }
  html, body {
    margin: 0;
    padding: 0;
    width: 1200px;
    height: 853px;
    overflow: hidden;
    background: var(--backdrop);
  }
  .canvas {
    position: relative;
    width: 1200px;
    height: 853px;
  }
  .card {
    position: absolute;
    top: 132px;
    width: 336px;
    height: 588px;
    border-radius: 12px;
    box-shadow: 0 6px 18px rgba(0,0,0,0.45);
    overflow: hidden;
  }
  .card-front { left: 243px; }
  .card-back { left: 696px; }

  .card-pattern {
    position: absolute;
    inset: 0;
  }
  .card-front .card-pattern {
    background: linear-gradient(160deg, var(--card-light-edge), var(--card-light));
  }
  .card-back .card-pattern {
    background: linear-gradient(160deg, var(--brand-blue-soft), var(--brand-blue));
  }

  .brand {
    position: absolute;
    display: flex;
    align-items: center;
    gap: 12px;
    font-family: 'Lato', sans-serif;
    font-weight: 700;
  }
  .brand-mark {
    width: 34px;
    height: 34px;
    border: 3px solid currentColor;
    border-radius: 3px;
    box-sizing: border-box;
    flex: none;
  }
  .brand-name {
    line-height: 1.05;
  }
  .brand-name .brand-primary {
    display: block;
    font-size: 34px;
    letter-spacing: 0.5px;
  }
  .brand-name .brand-secondary {
    display: block;
    font-size: 19px;
  }
  .card-front .brand {
    left: 53px;
    top: 82px;
    color: var(--brand-blue);
  }
  .card-back .brand {
    left: 58px;
    top: 466px;
    color: var(--white);
  }

  .contact {
    position: absolute;
    left: 35px;
    top: 449px;
    font-family: 'Lato', sans-serif;
    color: var(--text-grey);
  }
  .contact-name {
    margin: 0;
    font-family: 'Noto Serif', serif;
    font-weight: 700;
    font-size: 19px;
    color: var(--brand-blue);
    line-height: 1.2;
  }
  .contact-title {
    margin: 0 0 6px;
    font-size: 14.5px;
    line-height: 1.4;
  }
  .contact-list {
    list-style: none;
    margin: 0;
    padding: 0;
  }
  .contact-item {
    display: flex;
    align-items: center;
    gap: 5px;
    font-size: 14.5px;
    line-height: 21px;
  }
  .contact-icon {
    width: 10px;
    height: 10px;
    flex: none;
    color: var(--brand-green);
  }
  .web-domain { color: var(--brand-blue); }
</style>
</head>
<body>
<main class="canvas">
  <section class="card card-front" aria-label="Business card front">
    <div class="card-pattern" role="img" aria-label="Subtle light grey geometric cube line pattern"></div>

    <div class="brand">
      <span class="brand-mark" aria-hidden="true"></span>
      <span class="brand-name">
        <span class="brand-primary">BRANTLEY</span>
        <span class="brand-secondary">Advisory Group</span>
      </span>
    </div>

    <div class="contact">
      <h1 class="contact-name">Mark Brantley</h1>
      <p class="contact-title">Principal</p>
      <ul class="contact-list">
        <li class="contact-item">
          <svg class="contact-icon" viewBox="0 0 10 10" aria-hidden="true">
            <rect x="2.2" y="0.5" width="5.6" height="9" rx="1" fill="none" stroke="currentColor" stroke-width="1.2"/>
            <rect x="4.2" y="7.2" width="1.6" height="1" fill="currentColor"/>
          </svg>
          <span>425.318.2746</span>
        </li>
        <li class="contact-item">
          <svg class="contact-icon" viewBox="0 0 10 10" aria-hidden="true">
            <rect x="0.5" y="2" width="9" height="6.5" fill="currentColor"/>
            <path d="M1 2.5 L5 5.8 L9 2.5" fill="none" stroke="#ebebea" stroke-width="1"/>
          </svg>
          <span>mbrantley@brantleyag-example.com</span>
        </li>
        <li class="contact-item">
          <svg class="contact-icon" viewBox="0 0 10 10" aria-hidden="true">
            <circle cx="5" cy="5" r="4.5" fill="currentColor"/>
            <path d="M1 5 H9 M5 0.5 V9.5" stroke="#ebebea" stroke-width="0.8"/>
          </svg>
          <span>www.<span class="web-domain">brantleyag-example</span>.com</span>
        </li>
      </ul>
    </div>
  </section>

  <section class="card card-back" aria-label="Business card back">
    <div class="card-pattern" role="img" aria-label="Deep blue geometric cube line pattern"></div>

    <div class="brand">
      <span class="brand-mark" aria-hidden="true"></span>
      <span class="brand-name">
        <span class="brand-primary">BRANTLEY</span>
        <span class="brand-secondary">Advisory Group</span>
      </span>
    </div>
  </section>
</main>
</body>
</html>
```